Business Card Design Project

We need a logo design for a new company based in Southern California called "Norvale Security Services, Inc." We install security and camera systems for homeowners and business, to protect their assets.
Updates

Project Deadline Extended
Reason: LOGO Design completes in eight days. Would like that design decided before we finish the business cards. Thanks...

Target Market(s)

Homeowners and business owners looking for additional protection of their assets.

Industry/Entity Type

Security

Font styles to use
Serif

Requirements
Must have
• Company Name
Office# 909-472-3615
Service# 909-472-3616
email: NorvaleSecurity@brimwell.net
address: 48620 Thorncrest Lane Rancho Cucamonga, CA 91704
Nice to have
• Serving Southern California

```html
<!DOCTYPE html>
<html lang="en">
<head>
<meta charset="utf-8">
<title>Norvale Security Services – Business Card</title>
<link rel="stylesheet" href="https://fonts.googleapis.com/css2?family=Open+Sans:wght@400;600;700&display=swap">
<style>
  :root {
    --backdrop: #d9dde2;
    --paper: #f7f7f6;
    --red: #e3202a;
    --red-deep: #b50f18;
    --grey: #8a8c8f;
    --grey-dark: #6f7174;
    --grey-text: #5d5f62;
    --white: #ffffff;
  }
  * { margin: 0; padding: 0; box-sizing: border-box; }
  html, body { width: 1200px; height: 675px; overflow: hidden; }
  body {
    background: var(--backdrop);
    font-family: "Open Sans", Arial, sans-serif;
    position: relative;
  }
  .card {
    position: absolute;
    left: 160px; top: 86px;
    width: 880px; height: 503px;
    background: var(--paper);
    overflow: hidden;
    box-shadow: 0 6px 24px rgba(0,0,0,.18);
  }
  .card-shapes { position: absolute; inset: 0; }
  .brand {
    position: absolute;
    left: 150px; top: 120px;
    width: 420px;
    text-align: center;
  }
  .brand-mark {
    display: block;
    width: 64px; height: 64px;
    margin: 0 auto 22px;
    border-radius: 50%;
    background: var(--red);
  }
  .brand-name {
    font-weight: 700;
    font-size: 25px;
    font-variant: small-caps;
    letter-spacing: .5px;
    color: var(--grey-dark);
    white-space: nowrap;
  }
  .person {
    position: absolute;
    left: 300px; top: 292px;
    color: var(--white);
    display: flex; align-items: center; gap: 12px;
    white-space: nowrap;
  }
  .person-name { font-weight: 700; font-size: 26px; }
  .person-role {
    font-size: 17px;
    border-left: 2px solid var(--white);
    padding-left: 12px;
    line-height: 26px;
  }
  .contact {
    position: absolute;
    left: 70px; top: 340px;
    list-style: none;
    color: var(--white);
    font-size: 19px;
    line-height: 27px;
  }
  .contact li { display: flex; align-items: center; gap: 12px; }
  .contact svg { width: 18px; height: 18px; flex: none; }
  .address {
    position: absolute;
    left: 600px; top: 248px;
    display: flex; align-items: flex-start; gap: 14px;
    color: var(--white);
    font-size: 17px;
    line-height: 23px;
  }
  .address svg { width: 40px; height: 40px; flex: none; margin-top: 8px; }
  .tagline {
    position: absolute;
    left: 0; right: 0; top: 455px;
    text-align: center;
    padding-left: 240px;
    color: #eeeeee;
    font-size: 22px;
    letter-spacing: .3px;
  }
</style>
</head>
<body>
  <article class="card">
    <svg class="card-shapes" width="880" height="503" viewBox="0 0 880 503" aria-hidden="true">
      <defs>
        <linearGradient id="redBand" x1="0" y1="1" x2="1" y2="0">
          <stop offset="0" stop-color="var(--red-deep)"/>
          <stop offset="1" stop-color="var(--red)"/>
        </linearGradient>
      </defs>
      <path class="swoosh" d="M0 318 Q500 286 880 108 L880 122 Q500 300 0 330 Z" fill="var(--grey)"/>
      <path class="red-band" d="M0 338 Q500 306 880 130 L880 430 L0 430 Z" fill="url(#redBand)"/>
      <path class="base-band" d="M0 430 L548 430 L562 416 L576 430 L880 430 L880 503 L0 503 Z" fill="var(--grey)"/>
    </svg>

    <div class="brand">
      <span class="brand-mark"></span>
      <div class="brand-name">Norvale Security Services, Inc.</div>
    </div>

    <div class="person">
      <span class="person-name">Daniel Reyes</span>
      <span class="person-role">Director</span>
    </div>

    <ul class="contact">
      <li>
        <svg viewBox="0 0 20 20"><circle cx="10" cy="10" r="9" fill="none" stroke="#fff" stroke-width="1.4"/><path d="M7 5.5l2 2-1 1.3c.6 1.3 1.6 2.3 2.9 2.9l1.3-1 2 2-1.2 1.3c-3 0-7-4-7-7z" fill="#fff"/></svg>
        909-472-3615 [Office]
      </li>
      <li>
        <svg viewBox="0 0 20 20"><circle cx="10" cy="10" r="9" fill="none" stroke="#fff" stroke-width="1.4"/><path d="M7 5.5l2 2-1 1.3c.6 1.3 1.6 2.3 2.9 2.9l1.3-1 2 2-1.2 1.3c-3 0-7-4-7-7z" fill="#fff"/></svg>
        909-472-3616 [Service]
      </li>
      <li>
        <svg viewBox="0 0 20 20"><circle cx="10" cy="10" r="9" fill="none" stroke="#fff" stroke-width="1.4"/><rect x="5.5" y="7" width="9" height="6.5" fill="none" stroke="#fff" stroke-width="1.2"/><path d="M5.5 7l4.5 3.5L14.5 7" fill="none" stroke="#fff" stroke-width="1.2"/></svg>
        NorvaleSecurity@brimwell.net
      </li>
    </ul>

    <div class="address">
      <svg viewBox="0 0 40 40"><circle cx="20" cy="20" r="18.5" fill="none" stroke="#fff" stroke-width="1.6"/><path d="M20 9a6 6 0 0 0-6 6c0 4.5 6 11 6 11s6-6.5 6-11a6 6 0 0 0-6-6z" fill="#fff"/><circle cx="20" cy="15" r="2.2" fill="var(--red)"/><path d="M11 29h18" stroke="#fff" stroke-width="1.6"/></svg>
      <p>48620 Thorncrest Lane Rancho<br>Cucamonga,<br>CA 91704</p>
    </div>

    <p class="tagline">Serving Southern California</p>
  </article>
</body>
</html>
```